RWM Bricklaying business card

i need a business card designed for my bricklaying company.
I was also hoping to get a logo drawn up so i can put it on some t-shirts.
You can use any style or colours just as long as it lloks good. thanks Dalton

Industry/Entity Type

Business

Contact Information for Business Card

Dalton Briggs
RWM Bricklaying
0461937205
Any type of brick/blockwork
No job too small

```html
<!DOCTYPE html>
<html lang="en">
<head>
<meta charset="utf-8">
<title>RWM Bricklaying – Business Card</title>
<link rel="stylesheet" href="https://fonts.googleapis.com/css2?family=Open+Sans:wght@400;600&display=swap">
<style>
  :root {
    --stage: #000000;
    --stage-shade: #0b0b0b;
    --stage-shade-deep: #060606;
    --card-white: #ffffff;
    --panel-light: #f6f6f6;
    --panel-lighter: #fafafa;
    --ink: #333333;
    --brand-blue: #4a8fe0;
    --tagline-blue: #3d95dd;
    --back-blue: #548de3;
    --back-deep: #4a7cc9;
    --back-mid: #4f86d6;
    --back-soft: #6a9bdb;
    --back-pale: #72a3e8;
    --back-ghost: rgba(255, 255, 255, 0.07);
    --back-ghost-dark: rgba(40, 80, 150, 0.18);
  }
  * { margin: 0; padding: 0; box-sizing: border-box; }
  html, body {
    width: 1143px; height: 1200px; overflow: hidden;
    background: var(--stage);
    font-family: "Open Sans", sans-serif;
  }
  .stage {
    position: absolute; left: 0; top: 0;
    width: 1200px; height: 1260px;
    transform: scale(0.9525); transform-origin: 0 0;
  }
  .block { position: absolute; }

  /* stage shading blocks */
  .shade-a { left: 955px; top: 276px; width: 75px; height: 45px; background: var(--stage-shade); }
  .shade-b { left: 995px; top: 324px; width: 54px; height: 44px; background: var(--stage-shade); }
  .shade-c { left: 0; top: 582px; width: 178px; height: 46px; background: var(--stage-shade); }
  .shade-d { left: 0; top: 656px; width: 253px; height: 298px; background: var(--stage-shade-deep); }

  /* front card */
  .card-front {
    position: absolute; left: 253px; top: 222px; width: 690px; height: 383px;
    background: var(--card-white); overflow: hidden;
    box-shadow: 0 0 22px rgba(255, 255, 255, 0.35);
  }
  .front-panel-top { left: 537px; top: 0; width: 153px; height: 48px; background: var(--panel-lighter); }
  .front-panel-mid { left: 337px; top: 46px; width: 203px; height: 72px; background: var(--panel-lighter); }
  .front-panel-name { left: 337px; top: 153px; width: 353px; height: 123px; background: var(--panel-light); }

  .brand { position: absolute; left: 47px; top: 160px; display: flex; align-items: center; gap: 14px; }
  .brand-square { width: 34px; height: 34px; background: var(--brand-blue); flex: none; }
  .brand-name { font-size: 19px; font-weight: 600; letter-spacing: 4px; color: var(--ink); text-transform: uppercase; white-space: nowrap; }

  .contact { position: absolute; left: 458px; top: 165px; color: var(--ink); }
  .contact-name { font-size: 28px; font-weight: 400; line-height: 1.2; letter-spacing: -0.3px; }
  .contact-phone { font-size: 22px; font-weight: 400; line-height: 1.3; }

  .tagline {
    position: absolute; left: 47px; top: 326px;
    font-size: 21px; letter-spacing: 3.2px; color: var(--tagline-blue); white-space: nowrap;
  }

  /* back card */
  .card-back {
    position: absolute; left: 253px; top: 666px; width: 690px; height: 384px;
    background: var(--back-blue); overflow: hidden;
  }
  .back-ghost-name {
    position: absolute; left: 10px; top: 0; font-size: 150px; font-weight: 600;
    line-height: 1.2; color: var(--back-ghost); white-space: nowrap; letter-spacing: -2px;
  }
  .back-block-a { left: 469px; top: 15px; width: 117px; height: 41px; background: var(--back-mid); }
  .back-block-b { left: 328px; top: 59px; width: 145px; height: 51px; background: var(--back-mid); }
  .back-block-c { left: 587px; top: 60px; width: 93px; height: 33px; background: var(--back-pale); }
  .back-block-d { left: 328px; top: 130px; width: 254px; height: 89px; background: var(--back-soft); border: 1px solid var(--back-pale); }
  .back-block-e { left: 75px; top: 254px; width: 453px; height: 130px; background: var(--back-deep); }
  .back-ghost-trade {
    position: absolute; left: 28px; top: 318px; width: 640px;
    display: flex; justify-content: space-between;
    font-size: 68px; line-height: 1; color: var(--back-ghost-dark);
  }
</style>
</head>
<body>
<div class="stage">
  <div class="block shade-a"></div>
  <div class="block shade-b"></div>
  <div class="block shade-c"></div>
  <div class="block shade-d"></div>

  <section class="card-front" aria-label="Business card front">
    <div class="block front-panel-top"></div>
    <div class="block front-panel-mid"></div>
    <div class="block front-panel-name"></div>

    <div class="brand">
      <span class="brand-square"></span>
      <span class="brand-name">RWM Bricklaying</span>
    </div>

    <div class="contact">
      <p class="contact-name">Dalton Briggs</p>
      <p class="contact-phone">0461 937 205</p>
    </div>

    <p class="tagline">Any type of brick/blockwork No job too small</p>
  </section>

  <section class="card-back" aria-label="Business card back">
    <div class="block back-block-e"></div>
    <div class="block back-block-a"></div>
    <div class="block back-block-b"></div>
    <div class="block back-block-c"></div>
    <div class="block back-block-d"></div>
    <p class="back-ghost-name">RWM</p>
    <p class="back-ghost-trade" aria-label="Bricklaying"><span>B</span><span>R</span><span>I</span><span>C</span><span>K</span><span>L</span><span>A</span><span>Y</span><span>I</span><span>N</span><span>G</span></p>
  </section>
</div>
</body>
</html>
```